Business Card and Stationary Design

After the successful redesign of our logo we are wanting to follow suite and create a new business card and stationary design!

New Logo is attached, information required on the business card should contain a mixture of the following but layout/arrangement is up to the designer.

Happy if the national provider number and abn are on the back, and happy for them to be smaller than the rest.

I am also happy to receive single sided or weird and wonderful designs.

Name
Title
National Provider Number 7291
ABN 53 219 864 317
Level 3, 42 Marlow Street
Harlow Vale NSW 2391
Ph: 1300 987 214
Mobile: 0432 785 619
name@ferngatebuild.com.au
www.ferngatebuild.com.au

Target Market(s)

Professionals, Peers, Students, Suppliers...

Industry/Entity Type

Construction

Contact Information for Business Card

Listed in project description

Font styles to use
Other font styles liked:
• Century Gothic

Colors
0455a3
3176b5
ffffff

Requirements
Must have
• Professional Design, same color scheme as our logo
Nice to have
• Something that sets our apart from everyone else would be fantastic, open to size and shape and layout options, as long as they present professionally.
• Open to raised/embossed text, alternative materials, custom sizes, clear material
Should not have
• The color orange

```html
<!DOCTYPE html>
<html lang="en">
<head>
<meta charset="utf-8">
<title>Ferngate Build – Business Card</title>
<link rel="stylesheet" href="https://fonts.googleapis.com/css2?family=Source+Sans+3:wght@400;600;700&display=swap">
<style>
  :root {
    --navy: #1d3b8b;
    --ink: #333333;
    --card: #ececec;
    --pattern: #e2e2e2;
    --backdrop: #4b4b4b;
  }
  * { margin: 0; padding: 0; box-sizing: border-box; }
  html, body { width: 1200px; height: 720px; overflow: hidden; }
  body {
    background: var(--backdrop);
    font-family: "Source Sans 3", "Myriad Pro", sans-serif;
    position: relative;
  }
  .card {
    position: absolute;
    top: 203px;
    width: 450px;
    height: 277px;
    background: var(--card);
  }
  .card--front { left: 137px; }
  .card--back { left: 618px; }

  .brand {
    position: absolute;
    left: 24px;
    top: 26px;
    display: flex;
    align-items: center;
    gap: 12px;
  }
  .brand__square {
    width: 36px;
    height: 36px;
    background: var(--navy);
  }
  .brand__name {
    font-size: 31px;
    font-weight: 400;
    color: var(--navy);
    letter-spacing: 0.5px;
    line-height: 1;
  }

  .details {
    position: absolute;
    left: 80px;
    top: 92px;
    color: var(--ink);
    font-size: 13px;
    line-height: 16px;
  }
  .details__name {
    font-size: 17px;
    font-weight: 700;
    color: var(--navy);
    line-height: 19px;
  }
  .details__title { margin-bottom: 10px; }
  .details__label { font-weight: 600; color: var(--navy); }
  .details__web { font-weight: 600; color: var(--navy); }
  .details__address { margin-top: 11px; }
  .details__reg {
    margin-top: 12px;
    color: var(--navy);
  }
  .details__sep { margin: 0 5px; }

  .back__pattern {
    position: absolute;
    inset: 0;
    background: linear-gradient(180deg, var(--pattern), #e7e7e7);
  }
  .back__mark {
    position: absolute;
    left: 317px;
    top: 146px;
    width: 32px;
    height: 32px;
    background: var(--navy);
  }
</style>
</head>
<body>
  <section class="card card--front">
    <div class="brand">
      <span class="brand__square"></span>
      <span class="brand__name">ferngate build</span>
    </div>
    <div class="details">
      <div class="details__name">DANIEL HARPER</div>
      <div class="details__title">Managing Director</div>
      <div><span class="details__label">P:</span> 1300 987 214</div>
      <div><span class="details__label">M:</span> 0432 785 619</div>
      <div><span class="details__label">E:</span> name@ferngatebuild.com.au</div>
      <div class="details__web">www.ferngatebuild.com.au</div>
      <div class="details__address">Level 3, 42 Marlow Street, Harlow Vale NSW 2391</div>
      <div class="details__reg">ABN 53 219 864 317<span class="details__sep">|</span>National Provider Number : 7291</div>
    </div>
  </section>

  <section class="card card--back">
    <div class="back__pattern" role="img" aria-label="Faint repeating brand pattern across the card back"></div>
    <span class="back__mark"></span>
  </section>
</body>
</html>
```